EDDM Mailer for Copper Kettle Repair

We need an EDDM sized postcard for our auto repair business promoting that we now offer free pick up and delivery of vehicles in the Brookside area as well as free loaner vehicles. Our logo, and a copy of our current post card are attached for reference. Please promote the business in general and highlight the pick up drop off loaner service that is new.

```html
<!DOCTYPE html>
<html lang="en">
<head>
<meta charset="utf-8">
<title>Copper Kettle Repair – EDDM Postcard</title>
<link rel="stylesheet" href="https://fonts.googleapis.com/css2?family=Alfa+Slab+One&family=Arimo:wght@400&family=Montserrat:ital,wght@0,400;0,500;0,600;0,700;0,800;0,900;1,400;1,500;1,600;1,700;1,800;1,900&display=swap">
<style>
  :root {
    --backdrop: #8a8a8a;
    --ink: #1c1c1c;
    --panel-dark: #1f1f1f;
    --white: #ffffff;
    --text-grey: #6f6f6f;
    --brand-green: #2f8f1f;
    --brand-red: #d01515;
    --star: #f5b50a;
    --map-bg: #ececec;
  }
  * { margin: 0; padding: 0; box-sizing: border-box; }
  html, body { width: 855px; height: 1200px; overflow: hidden; }
  body { background: var(--backdrop); font-family: "Montserrat", sans-serif; color: var(--ink); position: relative; }

  .postcard { position: absolute; left: 91px; width: 674px; height: 495px; background: var(--white); overflow: hidden; }
  .postcard--front { top: 84px; }
  .postcard--back { top: 610px; }
  .postcard > svg.shapes { position: absolute; inset: 0; width: 674px; height: 495px; }
  .abs { position: absolute; }

  /* Brand name */
  .brand-name { font-family: "Montserrat", sans-serif; font-weight: 700; text-align: center; line-height: 1.05; letter-spacing: 1px; display: flex; align-items: center; justify-content: center; gap: 8px; white-space: nowrap; }
  .brand-name .dot { border-radius: 50%; flex: none; }
  .postcard--front .brand-name { left: 64px; top: 30px; width: 220px; color: var(--white); font-size: 16px; }
  .postcard--front .brand-name .dot { width: 16px; height: 16px; background: var(--white); }
  .postcard--back .brand-name { left: 70px; top: 50px; width: 270px; color: var(--ink); font-size: 22px; gap: 12px; }
  .postcard--back .brand-name .dot { width: 24px; height: 24px; background: var(--ink); }

  /* Front headline */
  .headline-top { left: 56px; top: 100px; font-family: "Alfa Slab One", serif; font-style: italic; color: var(--white); font-size: 27px; letter-spacing: 1px; }
  .headline-auto { left: 44px; top: 126px; font-weight: 900; font-style: italic; font-size: 62px; line-height: 1; letter-spacing: 1px;
    background: linear-gradient(180deg, #ffffff 0%, #cfcfcf 45%, #7d7d7d 70%, #d9d9d9 100%); -webkit-background-clip: text; background-clip: text; color: transparent; }
  .headline-repair { left: 40px; top: 182px; font-weight: 800; font-style: italic; font-size: 48px; line-height: 1; color: #dcdcdc; letter-spacing: -1px; white-space: nowrap; }
  .headline-repair .amp { font-weight: 400; color: var(--white); }
  .headline-pm { left: 42px; top: 248px; font-weight: 800; font-style: italic; font-size: 27px; line-height: 0.93; color: var(--ink); }
  .tagline { left: 32px; top: 313px; font-weight: 700; font-style: italic; font-size: 11px; line-height: 1.25; }
  .tagline .sub { color: var(--text-grey); }

  .badge-free { font-weight: 900; font-style: italic; font-size: 21px; color: var(--white); line-height: 1; }
  .badge-label { font-weight: 800; font-style: italic; font-size: 11px; color: var(--white); white-space: nowrap; display: flex; align-items: center; gap: 4px; }
  .badge-label .amp-dot { width: 13px; height: 13px; border-radius: 50%; background: var(--white); color: var(--brand-red); font-size: 9px; font-style: normal; display: inline-flex; align-items: center; justify-content: center; }
  .offer-copy { font-style: italic; font-size: 12px; line-height: 1.22; color: #2a2a2a; white-space: nowrap; }
  .offer-copy strong { font-weight: 800; }
  .offer-copy .area { color: var(--brand-red); }

  /* Shared bottom */
  .cta-bar { left: 40px; font-weight: 700; font-style: italic; color: var(--white); font-size: 14.5px; letter-spacing: 0.2px; white-space: nowrap; }
  .cta-bar .or { font-weight: 400; color: #cfcfcf; }
  .contact-phone { left: 68px; font-weight: 700; font-size: 21px; color: #2a2a2a; }
  .contact-line { font-size: 10.8px; line-height: 1.2; color: #2a2a2a; white-space: nowrap; }
  .contact-web { left: 407px; top: 458px; font-size: 10px; }
  .follow { left: 557px; color: var(--white); font-size: 10.5px; }
  .social-dots { display: flex; gap: 4px; margin-top: 6px; }
  .social-dots span { width: 13px; height: 13px; border-radius: 50%; background: var(--white); display: block; }

  /* Back: mailing area */
  .return-address { left: 429px; top: 21px; font-family: "Arimo", sans-serif; font-size: 10.3px; line-height: 1.22; }
  .indicia { left: 601px; top: 18px; width: 57px; height: 57px; border: 1px solid var(--ink); font-family: "Arimo", sans-serif; font-size: 6.9px; line-height: 1.32; text-align: center; padding-top: 5px; }
  .addressee { left: 429px; top: 85px; width: 183px; height: 37px; border: 1px solid var(--ink); font-family: "Arimo", sans-serif; font-size: 9px; }
  .addressee .route { position: absolute; right: 7px; top: 4px; }
  .addressee .name { position: absolute; left: 6px; top: 21px; }

  /* Back: car care */
  .care-complete { left: 42px; top: 156px; font-weight: 500; font-style: italic; font-size: 19px; color: var(--white); }
  .care-main { left: 41px; top: 179px; font-weight: 900; font-style: italic; font-size: 28px; line-height: 1;
    background: linear-gradient(180deg, #ffffff 0%, #c8c8c8 50%, #8a8a8a 75%, #d0d0d0 100%); -webkit-background-clip: text; background-clip: text; color: transparent; }
  .care-sub { left: 42px; top: 209px; font-weight: 600; font-style: italic; font-size: 15.5px; color: var(--white); }
  .care-includes { left: 40px; top: 241px; font-weight: 700; font-size: 11px; line-height: 1.2; color: var(--white); }
  .care-body { left: 39px; top: 272px; width: 196px; font-size: 7.7px; line-height: 1.2; color: #e6e6e6; }
  .feature { width: 90px; text-align: center; font-size: 8.6px; font-weight: 500; line-height: 1.1; color: var(--ink); }

  /* Back: review */
  .review-text { left: 408px; top: 175px; width: 220px; font-size: 9.2px; line-height: 1.18; color: #2a2a2a; }
  .review-name { left: 404px; top: 234px; font-weight: 800; font-style: italic; font-size: 9px; }
  .quote-mark { font-family: "Alfa Slab One", serif; font-size: 44px; line-height: 1; color: var(--ink); }
  .map-label { font-weight: 800; font-size: 7.4px; color: var(--brand-red); white-space: nowrap; }
</style>
</head>
<body>

<!-- ============ FRONT ============ -->
<section class="postcard postcard--front">
  <svg class="shapes" viewBox="0 0 674 495">
    <defs>
      <linearGradient id="frontLower" x1="0" y1="0" x2="1" y2="1">
        <stop offset="0" stop-color="#ffffff"/><stop offset="0.6" stop-color="#f3f3f3"/><stop offset="1" stop-color="#e6e6e6"/>
      </linearGradient>
      <linearGradient id="frontDark" x1="0" y1="0" x2="0" y2="1">
        <stop offset="0" stop-color="#1b1b1b"/><stop offset="0.7" stop-color="#2a2a2a"/><stop offset="1" stop-color="#161616"/>
      </linearGradient>
      <linearGradient id="silverBand" x1="0" y1="0" x2="1" y2="0">
        <stop offset="0" stop-color="#ededed"/><stop offset="0.5" stop-color="#cfcfcf"/><stop offset="1" stop-color="#9c9c9c"/>
      </linearGradient>
      <linearGradient id="photoWork" x1="0" y1="0" x2="1" y2="1">
        <stop offset="0" stop-color="#5a5a5a"/><stop offset="0.5" stop-color="#8f8f8f"/><stop offset="1" stop-color="#4a4a4a"/>
      </linearGradient>
      <linearGradient id="ctaBar" x1="0" y1="0" x2="1" y2="0">
        <stop offset="0" stop-color="#2b2b2b"/><stop offset="1" stop-color="#4a4a4a"/>
      </linearGradient>
    </defs>
    <rect width="674" height="495" fill="url(#frontLower)"/>
    <polygon points="0,0 430,0 405,245 0,245" fill="url(#frontDark)"/>
    <polygon points="0,245 404,245 388,308 0,308" fill="url(#silverBand)"/>
    <rect x="630" y="0" width="44" height="75" fill="#1a1a1a"/>
    <polygon points="383,0 674,0 674,10 592,328 303,328" fill="#ffffff"/>
    <polygon points="397,0 674,0 674,310 582,317 317,317" fill="url(#photoWork)" role="img" aria-label="Photo: mechanic working on an engine in the shop"/>
    <!-- pick-up badge -->
    <polygon points="87,353 157,353 151,377 81,377" fill="var(--brand-green)"/>
    <polygon points="32,378 172,378 166,406 32,406" fill="var(--ink)"/>
    <g fill="none" stroke="#2a2a2a" stroke-width="1.6">
      <rect x="55" y="355" width="16" height="18" rx="2"/>
      <line x1="52" y1="373" x2="74" y2="373"/>
      <circle cx="78" cy="362" r="4"/>
    </g>
    <!-- loaner badge -->
    <polygon points="424,349 505,349 497,378 417,378" fill="var(--brand-red)"/>
    <polygon points="377,378 518,378 510,406 383,406" fill="var(--ink)"/>
    <g fill="none" stroke="#2a2a2a" stroke-width="1.6">
      <path d="M384 372 v-8 l5 -9 h18 l5 9 v8 z"/>
      <line x1="384" y1="364" x2="412" y2="364"/>
    </g>
    <circle cx="408" cy="347" r="5.5" fill="none" stroke="#2a2a2a" stroke-width="1.3"/>
    <!-- CTA + footer -->
    <polygon points="0,414 468,414 461,439 0,439" fill="url(#ctaBar)"/>
    <polygon points="546,441 674,441 674,495 536,495" fill="var(--panel-dark)"/>
    <circle cx="45" cy="461" r="10" fill="#2a2a2a"/>
    <path d="M41 456 q-1 6 4 10 l2 -2 -2.4 -2 -1.4 1 q-2 -2 -2 -4 l1.3 -1 -1 -2.5 z" fill="#fff"/>
    <circle cx="234" cy="464" r="8.5" fill="#2a2a2a"/>
    <path d="M234 459 a3.4 3.4 0 0 1 3.4 3.4 c0 2.4 -3.4 5.6 -3.4 5.6 s-3.4 -3.2 -3.4 -5.6 a3.4 3.4 0 0 1 3.4 -3.4 z" fill="#fff"/>
    <circle cx="393" cy="464" r="8.5" fill="#2a2a2a"/>
    <g fill="none" stroke="#fff" stroke-width="0.9"><circle cx="393" cy="464" r="4.6"/><ellipse cx="393" cy="464" rx="2" ry="4.6"/><line x1="388.4" y1="464" x2="397.6" y2="464"/></g>
  </svg>

  <div class="abs brand-name"><span class="dot"></span><span>COPPER KETTLE<br>REPAIR</span></div>
  <div class="abs headline-top">HIGH-QUALITY</div>
  <div class="abs headline-auto">AUTO</div>
  <div class="abs headline-repair">REPAIR <span class="amp">&amp;</span></div>
  <div class="abs headline-pm">Preventative<br>maintenance!</div>
  <p class="abs tagline">We know your vehicle is important to you,<br><span class="sub">we’ll make it important to us too!</span></p>

  <div class="abs badge-free" style="left:90px;top:355px;">FREE</div>
  <div class="abs badge-label" style="left:44px;top:385px;">Pick-Up <span class="amp-dot">&amp;</span> Delivery!</div>
  <p class="abs offer-copy" style="left:178px;top:359px;">We’ll service your car and<br>bring it back—<strong>hassle-free!</strong><br><span class="area">in the <strong>Brookside area</strong></span></p>

  <div class="abs badge-free" style="left:424px;top:352px;font-size:22px;">FREE</div>
  <div class="abs badge-label" style="left:393px;top:384px;font-size:12px;">Loaner Vehicles!</div>
  <p class="abs offer-copy" style="left:530px;top:356px;">Stay on the move<br>while we work on<br>your car.</p>

  <div class="abs cta-bar" style="top:417px;">Visit us online <span class="or">or</span>&nbsp; call today to schedule&nbsp; your service!</div>
  <div class="abs contact-phone" style="top:449px;">555-014-0182</div>
  <div class="abs contact-line" style="left:247px;top:452px;">418 Orchard Lane,<br>Unit B, Millbrook</div>
  <div class="abs contact-line contact-web">CopperKettleRepair.com</div>
  <div class="abs follow" style="top:450px;">Follow us on<div class="social-dots"><span></span><span></span></div></div>
</section>

<!-- ============ BACK ============ -->
<section class="postcard postcard--back">
  <svg class="shapes" viewBox="0 0 674 495">
    <defs>
      <linearGradient id="backDark" x1="0" y1="0" x2="1" y2="0">
        <stop offset="0" stop-color="#1c1c1c"/><stop offset="0.6" stop-color="#262626"/><stop offset="1" stop-color="#3b3b3b"/>
      </linearGradient>
      <linearGradient id="handsPhoto" x1="0" y1="0" x2="1" y2="1">
        <stop offset="0" stop-color="#2a2a2a"/><stop offset="0.5" stop-color="#5e5e5e"/><stop offset="1" stop-color="#333"/>
      </linearGradient>
      <linearGradient id="enginePhoto" x1="0" y1="0" x2="1" y2="1">
        <stop offset="0" stop-color="#7a7a7a"/><stop offset="0.5" stop-color="#b0b0b0"/><stop offset="1" stop-color="#3f3f3f"/>
      </linearGradient>
      <linearGradient id="silverBand2" x1="0" y1="0" x2="1" y2="0">
        <stop offset="0" stop-color="#e8e8e8"/><stop offset="0.6" stop-color="#c9c9c9"/><stop offset="1" stop-color="#9a9a9a"/>
      </linearGradient>
      <linearGradient id="backLower" x1="0" y1="0" x2="1" y2="1">
        <stop offset="0" stop-color="#ffffff"/><stop offset="1" stop-color="#e7e7e7"/>
      </linearGradient>
      <linearGradient id="ctaBar2" x1="0" y1="0" x2="1" y2="0">
        <stop offset="0" stop-color="#2b2b2b"/><stop offset="1" stop-color="#4a4a4a"/>
      </linearGradient>
    </defs>
    <rect width="674" height="495" fill="url(#backLower)"/>
    <line x1="430" y1="129" x2="674" y2="129" stroke="#d5d5d5" stroke-width="0.8"/>
    <polygon points="0,141 400,141 345,414 0,414" fill="url(#backDark)"/>
    <polygon points="230,220 380,190 345,414 210,414" fill="url(#handsPhoto)" role="img" aria-label="Photo: mechanic's hands working under the hood"/>
    <polygon points="266,146 396,146 377,253 246,253" fill="#ffffff"/>
    <polygon points="274,150 390,150 372,247 253,247" fill="url(#enginePhoto)" role="img" aria-label="Photo: close-up of a car engine bay"/>
    <polygon points="0,343 334,343 320,410 0,410" fill="url(#silverBand2)"/>
    <!-- feature icons -->
    <g fill="#ffffff" stroke="#2a2a2a" stroke-width="1.6">
      <circle cx="83" cy="349" r="22"/><circle cx="176" cy="349" r="22"/><circle cx="264" cy="349" r="22"/>
    </g>
    <g fill="none" stroke="#2a2a2a" stroke-width="1.3">
      <circle cx="83" cy="349" r="9"/><circle cx="83" cy="349" r="3.5"/>
      <line x1="76" y1="356" x2="91" y2="342"/>
      <circle cx="176" cy="346" r="4.5"/><path d="M168 359 q8 -9 16 0"/><path d="M168 344 a8 8 0 0 1 16 0"/>
      <path d="M258 345 a6 6 0 0 1 12 0 z"/><circle cx="264" cy="349" r="3"/><circle cx="258" cy="357" r="3"/><circle cx="270" cy="357" r="3"/>
    </g>
    <!-- review frame -->
    <polyline points="440,156 636,156 622,245 548,245" fill="none" stroke="#9a9a9a" stroke-width="0.8"/>
    <line x1="402" y1="245" x2="497" y2="245" stroke="#9a9a9a" stroke-width="0.8"/>
    <g fill="var(--star)">
      <path id="star" d="M506 239 l1.9 3.9 4.3 .6 -3.1 3 .7 4.3 -3.8 -2 -3.8 2 .7 -4.3 -3.1 -3 4.3 -.6 z"/>
      <use href="#star" x="12"/><use href="#star" x="24"/><use href="#star" x="36"/><use href="#star" x="48"/>
    </g>
    <!-- map -->
    <polygon points="353,267 632,267 617,393 343,393" fill="#ffffff"/>
    <polygon points="356,270 628,270 614,390 347,390" fill="var(--map-bg)" role="img" aria-label="Map showing the shop's location"/>
    <path d="M511 340 a6 6 0 0 1 6 6 c0 5 -6 11 -6 11 s-6 -6 -6 -11 a6 6 0 0 1 6 -6 z" fill="var(--brand-red)"/>
    <circle cx="511" cy="346" r="2.2" fill="#fff"/>
    <!-- CTA + footer -->
    <polygon points="0,414 468,414 461,438 0,438" fill="url(#ctaBar2)"/>
    <polygon points="546,441 674,441 674,495 536,495" fill="var(--panel-dark)"/>
    <circle cx="45" cy="461" r="10" fill="#2a2a2a"/>
    <path d="M41 456 q-1 6 4 10 l2 -2 -2.4 -2 -1.4 1 q-2 -2 -2 -4 l1.3 -1 -1 -2.5 z" fill="#fff"/>
    <circle cx="234" cy="464" r="8.5" fill="#2a2a2a"/>
    <path d="M234 459 a3.4 3.4 0 0 1 3.4 3.4 c0 2.4 -3.4 5.6 -3.4 5.6 s-3.4 -3.2 -3.4 -5.6 a3.4 3.4 0 0 1 3.4 -3.4 z" fill="#fff"/>
    <circle cx="393" cy="464" r="8.5" fill="#2a2a2a"/>
    <g fill="none" stroke="#fff" stroke-width="0.9"><circle cx="393" cy="464" r="4.6"/><ellipse cx="393" cy="464" rx="2" ry="4.6"/><line x1="388.4" y1="464" x2="397.6" y2="464"/></g>
  </svg>

  <div class="abs brand-name"><span class="dot"></span><span>COPPER KETTLE<br>REPAIR</span></div>

  <p class="abs return-address">Copper Kettle Repair<br>418 Orchard Lane, Unit B<br>Millbrook, PA 17500</p>
  <div class="abs indicia">PRSRT STD<br>ECRWSS<br>U.S.POSTAGE<br>PAID<br>EDDM RETAIL</div>
  <div class="abs addressee"><span class="route">*****************ECRWSS****EDDM</span><span class="name">Local Postal Customer</span></div>

  <div class="abs care-complete">COMPLETE</div>
  <div class="abs care-main">CAR CARE</div>
  <div class="abs care-sub">FROM TOP TO BOTTOM!</div>
  <p class="abs care-includes">Including inspections<br>and emissions!</p>
  <p class="abs care-body">Don't trust your car to just any automotive repair shop. We have the reliable, experienced technicians to quickly diagnose what's wrong and fix it right the first time—saving you time, headaches AND money.</p>

  <p class="abs feature" style="left:38px;top:375px;">Trust in a timely,<br>full-service repair<br>facility</p>
  <p class="abs feature" style="left:131px;top:375px;">Enjoy<br>unparalleled<br>customer service</p>
  <p class="abs feature" style="left:219px;top:375px;">Work with<br>experienced and<br>caring technicians</p>

  <div class="abs quote-mark" style="left:412px;top:142px;">“</div>
  <p class="abs review-text">We had a great experience with Copper Kettle. We were able to schedule an appointment online, and they had one available the next day. They also have the ability to pay online as well.</p>
  <div class="abs review-name">— Dana K.</div>
  <div class="abs quote-mark" style="left:584px;top:228px;">”</div>

  <div class="abs map-label" style="left:520px;top:347px;">COPPER KETTLE REPAIR</div>

  <div class="abs cta-bar" style="top:417px;">Visit us online <span class="or">or</span>&nbsp; call today to schedule&nbsp; your service!</div>
  <div class="abs contact-phone" style="top:449px;">555-014-0182</div>
  <div class="abs contact-line" style="left:247px;top:452px;">418 Orchard Lane,<br>Unit B, Millbrook</div>
  <div class="abs contact-line contact-web">CopperKettleRepair.com</div>
  <div class="abs follow" style="top:450px;">Follow us on<div class="social-dots"><span></span><span></span></div></div>
</section>

</body>
</html>
```